FinTech company looking to revamp and expand client-facing interface for our financial models

Halvern Quotient currently has a very simple website that allows clients to interact with our financial models. We are looking to completely redesign the current site and add several extra pages to provide extra functionality. We want the design to have a modern, slick feel, that will work on both a desktop or a tablet. It should be straightforward for clients to move between different pages at any time, and clear from the layout how to interact with the more advanced features. We have included screenshots of existing pages in the attached design brief, as well as sketches of the functionality required by the new pages, but can't provide a direct link to the current site.
Target Market(s)
Professional investors that will be paying to access the interface
Industry/Entity Type
Finance
Number of Pages Required
4 page
Colors
Designer to choose colors to be used in the design.
Look and feel
Each slider illustrates characteristics of the customer's brand and the style your logo design should communicate.

```html
<!DOCTYPE html>
<html lang="en">
<head>
<meta charset="utf-8">
<title>Halvern Quotient — Models</title>
<link href="https://fonts.googleapis.com/css2?family=Montserrat:wght@400;500;600;700&display=swap" rel="stylesheet">
<style>
:root{
  --bg:#e8eff6;
  --brand:#2185d9;
  --brand-dark:#1b7ad0;
  --white:#ffffff;
  --row-alt:#f4f8fd;
  --text:#26313d;
  --muted:#8c99a8;
  --link:#2a86d6;
  --divider:#c9dcef;
  --fav:#f0505a;
}
*{margin:0;padding:0;box-sizing:border-box}
html,body{width:1200px;height:746px;overflow:hidden}
body{background:var(--bg);font-family:'Montserrat',sans-serif;color:var(--text);position:relative}
.topbar{position:absolute;left:0;top:0;width:1200px;height:67px;background:linear-gradient(90deg,var(--brand) 0%,var(--brand-dark) 60%,var(--brand) 100%);box-shadow:0 4px 14px rgba(33,133,217,.25);color:var(--white)}
.topbar .wordmark{position:absolute;left:150px;top:22px;font-size:19px;font-weight:500;letter-spacing:.2px}
.topbar a{position:absolute;top:26px;color:var(--white);text-decoration:none;font-size:12.5px;font-weight:500;display:flex;align-items:center;gap:6px}
.topbar a.dim{color:rgba(255,255,255,.7)}
.topbar .underline{position:absolute;bottom:0;height:2px;background:rgba(255,255,255,.85)}
.topbar svg{width:14px;height:14px;stroke:currentColor;fill:none;stroke-width:1.6}
.categories{position:absolute;left:150px;top:118px;width:900px;height:52px;background:var(--white);border-radius:3px}
.categories span{position:absolute;top:19px;font-size:11px;letter-spacing:.4px;color:var(--text)}
.categories span.active{color:var(--link)}
.categories span.fade{color:#b7c1cc}
.categories i{position:absolute;top:15px;height:22px;border-left:1px dashed var(--divider)}
.categories .active-bar{position:absolute;left:19px;bottom:0;width:69px;height:2px;background:var(--link)}
.categories .next{position:absolute;left:874px;top:18px;width:16px;height:14px;stroke:var(--link);fill:none;stroke-width:1.8}
.tool{position:absolute;top:198px;color:var(--link);font-size:13px;display:flex;align-items:center;gap:6px}
.tool svg{width:13px;height:13px;stroke:var(--link);fill:none;stroke-width:1.6}
.models{position:absolute;left:150px;top:226px;width:900px;height:464px;border-radius:4px;overflow:hidden;background:var(--white)}
.row{position:relative;height:70px}
.row.head{height:45px;background:var(--row-alt)}
.row:nth-child(odd):not(.head){background:var(--row-alt)}
.cell{position:absolute;font-size:13px;top:50%;transform:translateY(-50%);white-space:nowrap;line-height:16px}
.head .cell{color:var(--muted);font-size:12.5px}
.star{position:absolute;left:10px;top:50%;transform:translateY(-50%);width:9px;height:9px}
.star path{fill:none;stroke:#b9c3ce;stroke-width:1.2}
.star.on path{fill:var(--fav);stroke:var(--fav)}
.c-id{left:25px}.c-sec{left:92px}.c-time{left:175px}.c-q{left:263px}
.c-1{left:341px}.c-2{left:410px}.c-3{left:478px}.c-4{left:553px}
.c-5{left:625px}.c-6{left:696px}.c-7{left:766px}.c-8{left:833px}
.head .c-id{left:14px}.head .c-sec{left:90px}.head .c-time{left:172px}.head .c-q{left:260px}
.head .c-1{left:340px}.head .c-2{left:409px}.head .c-3{left:480px}.head .c-4{left:551px}
.head .c-5{left:624px}.head .c-6{left:695px}.head .c-7{left:766px}.head .c-8{left:838px}
</style>
</head>
<body>
<header class="topbar">
  <div class="wordmark">Halvern</div>
  <a class="dim" style="left:276px">250D</a>
  <a style="left:340px">83D</a>
  <a style="left:397px">42D</a>
  <div class="underline" style="left:268px;width:51px"></div>
  <a class="dim" style="left:554px"><svg viewBox="0 0 16 16"><path d="M2 8l6-5 6 5M4 7v7h8V7"/></svg>Models</a>
  <div class="underline" style="left:551px;width:74px"></div>
  <a style="left:661px"><svg viewBox="0 0 16 16"><circle cx="3" cy="3" r="1.2"/><circle cx="8" cy="3" r="1.2"/><circle cx="13" cy="3" r="1.2"/><circle cx="3" cy="8" r="1.2"/><circle cx="8" cy="8" r="1.2"/><circle cx="13" cy="8" r="1.2"/><circle cx="3" cy="13" r="1.2"/><circle cx="8" cy="13" r="1.2"/></svg>Portfolio Builder</a>
  <a style="left:820px"><svg viewBox="0 0 16 16"><path d="M8 2l6 3-6 3-6-3zM2 8l6 3 6-3M2 11l6 3 6-3"/></svg>Sensitivities</a>
  <a style="left:958px"><svg viewBox="0 0 16 16"><path d="M8 1.5l2 4.2 4.5.6-3.3 3.1.8 4.5L8 11.7l-4 2.2.8-4.5L1.5 6.3 6 5.7z"/></svg>Favourites</a>
</header>

<nav class="categories">
  <span class="active" style="left:26px">EQUITIES</span><i style="left:101px"></i>
  <span style="left:123px">ETFS</span><i style="left:174px"></i>
  <span style="left:193px">PAIRS</span><i style="left:249px"></i>
  <span style="left:270px">ETF PAIRS</span><i style="left:352px"></i>
  <span style="left:371px">FACTORS</span><i style="left:448px"></i>
  <span style="left:468px">EQUITIES</span><i style="left:542px"></i>
  <span style="left:564px">ETFS</span><i style="left:615px"></i>
  <span style="left:634px">PAIRS</span><i style="left:690px"></i>
  <span style="left:712px">ETF PAIRS</span><i style="left:793px"></i>
  <span class="fade" style="left:812px">FACTORS</span>
  <svg class="next" viewBox="0 0 16 14"><path d="M1 7h13M9 2l5 5-5 5"/></svg>
  <div class="active-bar"></div>
</nav>

<div class="tool" style="left:150px"><svg viewBox="0 0 14 14"><path d="M1 1.5h12L8.3 7v5L5.7 13V7z"/></svg>Filter</div>
<div class="tool" style="right:150px"><svg viewBox="0 0 14 14"><path d="M6 2H1.5v10.5H12V8M8 1h5v5M13 1L6.5 7.5"/></svg>Export</div>

<section class="models">
  <div class="row head">
    <span class="cell c-id">ID ⌄</span><span class="cell c-sec">Sector</span><span class="cell c-time">Time</span><span class="cell c-q">Quality</span>
    <span class="cell c-1">Stat 1</span><span class="cell c-2">Stat 2</span><span class="cell c-3">Stat 3</span><span class="cell c-4">Stat 4</span>
    <span class="cell c-5">Stat 5</span><span class="cell c-6">Stat 6</span><span class="cell c-7">Stat 7</span><span class="cell c-8">Stat 8</span>
  </div>
  <div class="row"><svg class="star" viewBox="0 0 10 10"><path d="M5 .8l1.3 2.7 2.9.4-2.1 2 .5 2.9L5 7.4 2.4 8.8l.5-2.9-2.1-2 2.9-.4z"/></svg><span class="cell c-id">Model 1</span><span class="cell c-sec">Materials</span><span class="cell c-time">2019-07-03<br>12:15:00.000</span><span class="cell c-q">30.2888</span><span class="cell c-1">2.01574</span><span class="cell c-2">23.305</span><span class="cell c-3">-0.149368</span><span class="cell c-4">22.3054</span><span class="cell c-5">4.63714</span><span class="cell c-6">0.945706</span><span class="cell c-7">2.81949</span><span class="cell c-8">2.60858</span></div>
  <div class="row"><svg class="star on" viewBox="0 0 10 10"><path d="M5 .8l1.3 2.7 2.9.4-2.1 2 .5 2.9L5 7.4 2.4 8.8l.5-2.9-2.1-2 2.9-.4z"/></svg><span class="cell c-id">Model 2</span><span class="cell c-sec">Materials</span><span class="cell c-time">2019-07-03<br>12:15:00.000</span><span class="cell c-q">30.2888</span><span class="cell c-1">2.01574</span><span class="cell c-2">23.305</span><span class="cell c-3">-0.149368</span><span class="cell c-4">22.3054</span><span class="cell c-5">4.63714</span><span class="cell c-6">0.945706</span><span class="cell c-7">2.81949</span><span class="cell c-8">2.60858</span></div>
  <div class="row"><svg class="star" viewBox="0 0 10 10"><path d="M5 .8l1.3 2.7 2.9.4-2.1 2 .5 2.9L5 7.4 2.4 8.8l.5-2.9-2.1-2 2.9-.4z"/></svg><span class="cell c-id">Model 3</span><span class="cell c-sec">Materials</span><span class="cell c-time">2019-07-03<br>12:15:00.000</span><span class="cell c-q">30.2888</span><span class="cell c-1">2.01574</span><span class="cell c-2">23.305</span><span class="cell c-3">-0.149368</span><span class="cell c-4">22.3054</span><span class="cell c-5">4.63714</span><span class="cell c-6">0.945706</span><span class="cell c-7">2.81949</span><span class="cell c-8">2.60858</span></div>
  <div class="row"><svg class="star" viewBox="0 0 10 10"><path d="M5 .8l1.3 2.7 2.9.4-2.1 2 .5 2.9L5 7.4 2.4 8.8l.5-2.9-2.1-2 2.9-.4z"/></svg><span class="cell c-id">Model 4</span><span class="cell c-sec">Materials</span><span class="cell c-time">2019-07-03<br>12:15:00.000</span><span class="cell c-q">30.2888</span><span class="cell c-1">2.01574</span><span class="cell c-2">23.305</span><span class="cell c-3">-0.149368</span><span class="cell c-4">22.3054</span><span class="cell c-5">4.63714</span><span class="cell c-6">0.945706</span><span class="cell c-7">2.81949</span><span class="cell c-8">2.60858</span></div>
  <div class="row"><svg class="star" viewBox="0 0 10 10"><path d="M5 .8l1.3 2.7 2.9.4-2.1 2 .5 2.9L5 7.4 2.4 8.8l.5-2.9-2.1-2 2.9-.4z"/></svg><span class="cell c-id">Model 5</span><span class="cell c-sec">Materials</span><span class="cell c-time">2019-07-03<br>12:15:00.000</span><span class="cell c-q">30.2888</span><span class="cell c-1">2.01574</span><span class="cell c-2">23.305</span><span class="cell c-3">-0.149368</span><span class="cell c-4">22.3054</span><span class="cell c-5">4.63714</span><span class="cell c-6">0.945706</span><span class="cell c-7">2.81949</span><span class="cell c-8">2.60858</span></div>
  <div class="row"><svg class="star" viewBox="0 0 10 10"><path d="M5 .8l1.3 2.7 2.9.4-2.1 2 .5 2.9L5 7.4 2.4 8.8l.5-2.9-2.1-2 2.9-.4z"/></svg><span class="cell c-id">Model 6</span><span class="cell c-sec">Materials</span><span class="cell c-time">2019-07-03<br>12:15:00.000</span><span class="cell c-q">30.2888</span><span class="cell c-1">2.01574</span><span class="cell c-2">23.305</span><span class="cell c-3">-0.149368</span><span class="cell c-4">22.3054</span><span class="cell c-5">4.63714</span><span class="cell c-6">0.945706</span><span class="cell c-7">2.81949</span><span class="cell c-8">2.60858</span></div>
</section>
</body>
</html>
```